Need Business Card for eLearning Company

Need a business card designed for our company, CareerPathlane.

CareerPathlane has developed a complete 12 lesson eLearning course to teach you the skills you need to present yourself in a job interview. The course uses advanced learning techniques in the multimedia videos, plus contains quizzes and additional exercises to insure you get the course and can walk into any interview with confidence and ease, and get the job.

www.careerpathlane-demo.com

Attached is our logo

Industry/Entity Type

Business

```html
<!DOCTYPE html>
<html lang="en">
<head>
<meta charset="utf-8">
<title>CareerPathlane Business Card</title>
<link rel="stylesheet" href="https://fonts.googleapis.com/css2?family=Jost:wght@400;600&display=swap">
<style>
  :root {
    --backdrop: #e4e2df;
    --card: #f4f4f2;
    --plum: #7d1a6f;
    --leaf: #7fa520;
    --ink: #4a4a4a;
    --shadow: rgba(0, 0, 0, 0.14);
  }
  * { margin: 0; padding: 0; box-sizing: border-box; }
  html, body {
    width: 1200px;
    height: 900px;
    overflow: hidden;
    background: var(--backdrop);
    font-family: "Jost", "Century Gothic", sans-serif;
    color: var(--ink);
  }
  .stage {
    position: relative;
    width: 1200px;
    height: 900px;
  }
  .card {
    position: absolute;
    top: 152px;
    width: 340px;
    height: 596px;
    background: var(--card);
    box-shadow: 0 6px 18px var(--shadow);
  }
  .card--front { left: 220px; }
  .card--back { left: 640px; }

  /* Front */
  .brand {
    position: absolute;
    top: 34px;
    left: 30px;
    display: flex;
    align-items: center;
    gap: 12px;
  }
  .brand__mark {
    width: 22px;
    height: 22px;
    background: var(--ink);
    border-radius: 3px;
  }
  .brand__name {
    font-size: 30px;
    font-weight: 400;
    color: var(--ink);
    letter-spacing: 0.2px;
  }
  .person {
    position: absolute;
    top: 180px;
    left: 60px;
  }
  .person__name {
    font-size: 24px;
    font-weight: 400;
    color: var(--plum);
    line-height: 1.1;
  }
  .person__title {
    font-size: 17px;
    text-transform: uppercase;
    letter-spacing: 0.6px;
    line-height: 1.3;
  }
  .contact {
    position: absolute;
    top: 320px;
    left: 60px;
    font-size: 14px;
    line-height: 1.35;
    list-style: none;
  }
  .contact__label {
    display: inline-block;
    width: 16px;
    color: var(--plum);
  }
  .address {
    position: absolute;
    top: 392px;
    left: 76px;
    font-size: 16px;
    font-style: normal;
    line-height: 1.25;
  }
  .site {
    position: absolute;
    left: 76px;
    font-size: 15px;
    font-weight: 600;
    color: var(--plum);
  }
  .card--front .site { top: 476px; }

  /* Back */
  .feature-art {
    position: absolute;
    top: 40px;
    left: 40px;
    width: 260px;
    height: 250px;
    border-radius: 50%;
    background: radial-gradient(circle at 40% 40%, var(--plum) 0%, #8c4a7e 45%, var(--leaf) 100%);
    opacity: 0.85;
  }
  .card--back .site {
    left: auto;
    right: 24px;
    bottom: 40px;
    font-size: 13px;
  }
</style>
</head>
<body>
<main class="stage">
  <section class="card card--front">
    <div class="brand">
      <span class="brand__mark"></span>
      <span class="brand__name">CareerPathlane</span>
    </div>
    <div class="person">
      <p class="person__name">Dana Whitcombe</p>
      <p class="person__title">Principal Consultant</p>
    </div>
    <ul class="contact">
      <li><span class="contact__label">T</span>(555)014-2738</li>
      <li><span class="contact__label">E</span>support@careerpathlane-demo.com</li>
    </ul>
    <address class="address">240 Harbor Lane Suite 12,<br>Fairview, WA 98000</address>
    <p class="site">www.careerpathlane-demo.com</p>
  </section>

  <section class="card card--back">
    <div class="feature-art" role="img" aria-label="Cluster of purple and green speech bubbles"></div>
    <p class="site">www.careerpathlane-demo.com</p>
  </section>
</main>
</body>
</html>
```